Halvenor Crest Partners

Please look at the logo that we've just received and based on it provide us with the business card designs.

Industry/Entity Type

Business

Requirements
Must have
• Dummy text, so later on we can add the exact names and titles.

```html
<!DOCTYPE html>
<html lang="en">
<head>
<meta charset="utf-8">
<title>Halvenor Crest Partners – Business Card</title>
<link rel="stylesheet" href="https://fonts.googleapis.com/css2?family=Cinzel:wght@500&family=Questrial&display=swap">
<style>
  :root {
    --page-bg: #e6e2dc;
    --card-top: #f3f4f6;
    --card-top-shade: #dfe2e7;
    --navy: #1c2a6b;
    --navy-deep: #121c4d;
    --tagline-grey: #6b6e75;
    --silver: #b9bec8;
    --name-white: #f1f1f4;
    --detail-tan: #d8c0a4;
  }
  html, body {
    margin: 0;
    padding: 0;
    width: 1200px;
    height: 970px;
    overflow: hidden;
    background: var(--page-bg);
  }
  .canvas {
    position: relative;
    width: 1200px;
    height: 970px;
  }
  .business-card {
    position: absolute;
    left: 80px;
    top: 187px;
    width: 1040px;
    height: 595px;
    border-radius: 30px;
    overflow: hidden;
    background: linear-gradient(160deg, var(--card-top) 0%, var(--card-top-shade) 100%);
    box-shadow: 0 18px 40px rgba(40, 35, 30, 0.22);
  }
  .card-band {
    position: absolute;
    inset: 0;
    width: 100%;
    height: 100%;
  }
  .brand {
    position: absolute;
    left: 62px;
    top: 98px;
    display: flex;
    align-items: center;
    gap: 30px;
  }
  .brand-square {
    width: 96px;
    height: 96px;
    background: var(--navy);
    flex: none;
  }
  .brand-text {
    display: flex;
    flex-direction: column;
  }
  .brand-name {
    margin: 0;
    font-family: "Cinzel", serif;
    font-weight: 500;
    font-size: 66px;
    line-height: 1;
    color: var(--navy);
  }
  .brand-tagline {
    margin: 6px 0 0 2px;
    font-family: "Questrial", sans-serif;
    font-size: 26px;
    letter-spacing: 5px;
    line-height: 1;
    color: var(--tagline-grey);
  }
  .holder {
    position: absolute;
    left: 57px;
    top: 356px;
  }
  .holder-name {
    margin: 0;
    font-family: "Cinzel", serif;
    font-weight: 500;
    font-size: 34px;
    line-height: 1.1;
    color: var(--name-white);
    letter-spacing: 1px;
  }
  .holder-title {
    margin: 0;
    font-family: "Questrial", sans-serif;
    font-size: 25px;
    color: var(--name-white);
  }
  .contact-list {
    position: absolute;
    left: 57px;
    top: 446px;
    margin: 0;
    padding: 0;
    list-style: none;
    font-family: "Questrial", sans-serif;
    font-size: 27px;
    color: var(--detail-tan);
  }
  .contact-list li {
    display: flex;
    align-items: center;
    gap: 10px;
    height: 35px;
  }
  .contact-icon {
    width: 24px;
    height: 24px;
    flex: none;
  }
  .address {
    position: absolute;
    right: 50px;
    top: 482px;
    margin: 0;
    text-align: right;
    font-family: "Questrial", sans-serif;
    font-style: normal;
    font-size: 27px;
    line-height: 35px;
    color: var(--detail-tan);
  }
</style>
</head>
<body>
<main class="canvas">
  <section class="business-card" aria-label="Business card">
    <svg class="card-band" viewBox="0 0 1040 595" preserveAspectRatio="none" aria-hidden="true">
      <defs>
        <linearGradient id="navyFill" x1="0" y1="0" x2="0" y2="1">
          <stop offset="0" stop-color="var(--navy)"/>
          <stop offset="1" stop-color="var(--navy-deep)"/>
        </linearGradient>
      </defs>
      <path class="divider-line" fill="none" stroke="var(--silver)" stroke-width="3"
            d="M0 326 Q520 296 1040 326"/>
      <path class="navy-band" fill="url(#navyFill)"
            d="M0 338 Q520 308 1040 338 L1040 595 L0 595 Z"/>
    </svg>

    <div class="brand">
      <div class="brand-square"></div>
      <div class="brand-text">
        <h1 class="brand-name">Halvenor</h1>
        <p class="brand-tagline">CREST PARTNERS</p>
      </div>
    </div>

    <div class="holder">
      <h2 class="holder-name">Daniel Reed</h2>
      <p class="holder-title">Founder</p>
    </div>

    <ul class="contact-list">
      <li>
        <svg class="contact-icon" viewBox="0 0 24 24" aria-hidden="true">
          <rect x="5" y="2" width="14" height="20" rx="2" fill="none" stroke="var(--detail-tan)" stroke-width="2.2"/>
          <rect x="8" y="5" width="8" height="11" fill="var(--detail-tan)"/>
        </svg>
        <span>(555) 014-2278</span>
      </li>
      <li>
        <svg class="contact-icon" viewBox="0 0 24 24" aria-hidden="true">
          <rect x="2" y="5" width="20" height="14" fill="none" stroke="var(--detail-tan)" stroke-width="2"/>
          <path d="M2 5 L12 13 L22 5 M2 19 L9 11 M22 19 L15 11" fill="none" stroke="var(--detail-tan)" stroke-width="1.8"/>
        </svg>
        <span>info@halvenorcrest.com</span>
      </li>
      <li>
        <svg class="contact-icon" viewBox="0 0 24 24" aria-hidden="true">
          <circle cx="12" cy="12" r="10" fill="none" stroke="var(--detail-tan)" stroke-width="2"/>
          <ellipse cx="12" cy="12" rx="4.5" ry="10" fill="none" stroke="var(--detail-tan)" stroke-width="1.5"/>
          <path d="M2 12 H22 M4 7 H20 M4 17 H20" stroke="var(--detail-tan)" stroke-width="1.5"/>
        </svg>
        <span>www.halvenorcrest.com</span>
      </li>
    </ul>

    <address class="address">
      PO BOX 480 Harbour Lane<br>
      5th street Lindale
    </address>
  </section>
</main>
</body>
</html>
```